Real Estate Sales Brokerage

Design a modern and fresh looking standard size business card, incorporate our logo's color scheme and modern appearance with head shot photo on front side and incorporate our log on the back side

Target Market(s)

Residential Home sales

Industry/Entity Type

Real Estate Agent

Font styles to use
Sans Serif

Colors

Designer to choose colors to be used in the design.

Requirements
Must have
• fresh, modern, not too busy, incorporate head shot in front of the card, incorporate logo in front and back of the card. Use logo design scheme as appropriate.
Nice to have
• horizontal and vertical options to compare would be nice.

```html
<!DOCTYPE html>
<html lang="en">
<head>
<meta charset="utf-8">
<title>Harbor Crest Realty – Business Card</title>
<link rel="stylesheet" href="https://fonts.googleapis.com/css2?family=Montserrat:wght@600;700&family=Roboto:wght@400;500&display=swap">
<style>
  :root {
    --olive: #5f6131;
    --olive-light: #7a7c43;
    --olive-dark: #505228;
    --yellow: #f2d230;
    --white: #ffffff;
    --grey-text: #555555;
    --backdrop: #d9d9d9;
    --photo-top: #e9ecef;
    --photo-bottom: #2f4f8f;
  }
  * { margin: 0; padding: 0; box-sizing: border-box; }
  html, body { width: 1200px; height: 801px; overflow: hidden; }
  body {
    background: var(--backdrop);
    font-family: "Roboto", sans-serif;
    display: flex;
    align-items: center;
    justify-content: center;
    gap: 40px;
  }
  .card {
    position: relative;
    width: 540px;
    height: 309px;
    overflow: hidden;
    box-shadow: 0 6px 18px rgba(0,0,0,0.18);
  }
  .card-front { background: var(--white); }
  .card-back {
    background: radial-gradient(ellipse at 40% 45%, var(--olive-light) 0%, var(--olive) 55%, var(--olive-dark) 100%);
    display: flex;
    flex-direction: column;
    align-items: center;
    justify-content: center;
  }
  .headshot {
    position: absolute;
    right: 20px;
    top: 22px;
    width: 220px;
    height: 150px;
    background: linear-gradient(180deg, var(--photo-top) 0%, #c9d0da 45%, var(--photo-bottom) 100%);
  }
  .front-waves { position: absolute; inset: 0; width: 100%; height: 100%; }
  .brand {
    position: absolute;
    display: flex;
    align-items: center;
    gap: 8px;
    font-family: "Montserrat", sans-serif;
    font-weight: 600;
    text-transform: uppercase;
  }
  .brand-front { left: 28px; top: 38px; color: var(--olive); font-size: 12px; letter-spacing: 1px; }
  .brand-front .brand-mark { width: 14px; height: 14px; background: var(--yellow); }
  .person { position: absolute; left: 28px; top: 112px; }
  .person-name {
    font-family: "Montserrat", sans-serif;
    font-weight: 700;
    font-size: 22px;
    color: var(--yellow);
    letter-spacing: 1px;
  }
  .person-title {
    font-size: 11px;
    color: var(--grey-text);
    letter-spacing: 2px;
    margin-top: 2px;
  }
  .contact-list {
    position: absolute;
    left: 28px;
    bottom: 18px;
    list-style: none;
    color: var(--white);
    font-size: 11px;
    letter-spacing: 0.8px;
  }
  .contact-list li { display: flex; align-items: center; gap: 10px; height: 16px; }
  .contact-list svg { width: 10px; height: 10px; fill: none; stroke: var(--yellow); stroke-width: 1.6; flex: none; }
  .address {
    position: absolute;
    right: 22px;
    bottom: 60px;
    text-align: right;
    color: var(--white);
    font-size: 10.5px;
    letter-spacing: 0.6px;
    line-height: 1.4;
  }
  .address .site { color: var(--yellow); font-weight: 500; margin-top: 4px; }
  .brand-back { color: var(--white); font-size: 26px; letter-spacing: 2px; gap: 14px; }
  .brand-back .brand-mark { width: 26px; height: 26px; background: var(--white); }
  .back-site {
    margin-top: 26px;
    color: var(--white);
    font-size: 12px;
    font-weight: 500;
    letter-spacing: 1.5px;
  }
  .card-back .brand { position: static; }
</style>
</head>
<body>

  <section class="card card-front">
    <div class="headshot" role="img" aria-label="Head shot of the agent in a navy suit and red tie"></div>
    <svg class="front-waves" viewBox="0 0 540 309" preserveAspectRatio="none" aria-hidden="true">
      <path d="M0 194 C140 184 240 168 330 150 C420 132 480 110 540 92 L540 309 L0 309 Z" fill="var(--yellow)"/>
      <path d="M0 206 C140 196 240 181 330 163 C420 145 480 124 540 106 L540 309 L0 309 Z" fill="var(--olive)"/>
    </svg>

    <div class="brand brand-front"><span class="brand-mark"></span>Harbor Crest Realty</div>

    <div class="person">
      <div class="person-name">DAN ELLISON</div>
      <div class="person-title">DIRECTOR</div>
    </div>

    <ul class="contact-list">
      <li><svg viewBox="0 0 10 10"><rect x="2" y="1" width="6" height="8" rx="1"/></svg>555 010 2040</li>
      <li><svg viewBox="0 0 10 10"><path d="M2 1 L4 3 L3 4.5 C4 6 5 7 5.5 7 L7 6 L9 8 L7.5 9.5 C4 9 1 6 0.5 2.5 Z"/></svg>555 010 2041</li>
      <li><svg viewBox="0 0 10 10"><rect x="1" y="4" width="8" height="4"/><rect x="3" y="1" width="4" height="3"/></svg>+55 501 0234</li>
      <li><svg viewBox="0 0 10 10"><rect x="1" y="2" width="8" height="6"/><path d="M1 2 L5 5.5 L9 2"/></svg>dan@harborcrestre.com</li>
    </ul>

    <div class="address">
      <div>418 Maple Ave, Oakdale</div>
      <div>CA 95361, Amerika Serikat</div>
      <div class="site">www.harborcrestre.com</div>
    </div>
  </section>

  <section class="card card-back">
    <div class="brand brand-back"><span class="brand-mark"></span>Harbor Crest Realty</div>
    <div class="back-site">www.harborcrestre.com</div>
  </section>

</body>
</html>
```